I need a business card for myself, being a proprietor of a funeral parlor based in Manila. I'd like the card to have either of the following:
White Font on Black Background
or
Black Font on White Background
No logo is needed however I will appreciate any efforts to show a symbol of eternal happiness, aptly designed with above mentioned colors in mind.
Company name, address and contact on the lower right corner.
Logo or symbol anywhere.
Quillstone Funeral Services
+639174826351
darvik4521@pelmora.com
corner of Brisco Avenue and Velhurst Street
Makati City, Philippines
Thank you.
Update: Please include a small dove in your design. You are free to choose where you would like it on the card.

```html
<!DOCTYPE html>
<html lang="en">
<head>
<meta charset="utf-8">
<title>Quillstone Funeral Services — Business Card</title>
<link rel="stylesheet" href="https://fonts.googleapis.com/css2?family=Libre+Baskerville:wght@400;700&display=swap">
<style>
  :root {
    --page-bg: #ffffff;
    --card-black: #0b0b0b;
    --ink-white: #ffffff;
    --dove-tone-light: #3a3a3a;
    --dove-tone-dark: #1c1c1c;
  }
  html, body {
    margin: 0;
    padding: 0;
    width: 1200px;
    height: 1000px;
    overflow: hidden;
    background: var(--page-bg);
  }
  .canvas {
    position: relative;
    width: 1200px;
    height: 1000px;
  }
  .business-card {
    position: absolute;
    left: 150px;
    top: 250px;
    width: 900px;
    height: 500px;
    background: var(--card-black);
    overflow: hidden;
    box-shadow: 0 12px 30px rgba(0, 0, 0, 0.25);
  }
  .card-ring {
    position: absolute;
    inset: 0;
  }
  .dove-symbol {
    position: absolute;
    left: 70px;
    top: 95px;
    width: 230px;
    height: 220px;
    border-radius: 40% 60% 50% 50%;
    background: radial-gradient(circle at 60% 45%, var(--dove-tone-light), var(--dove-tone-dark));
  }
  .contact-block {
    position: absolute;
    right: 45px;
    bottom: 42px;
    text-align: right;
    color: var(--ink-white);
    font-family: "Libre Baskerville", Georgia, serif;
    font-size: 23px;
    line-height: 1.38;
  }
  .contact-block p {
    margin: 0;
  }
  .company-name {
    font-weight: 700;
    font-size: 27px;
    margin-bottom: 2px !important;
  }
  .city-line {
    font-weight: 700;
  }
</style>
</head>
<body>
  <main class="canvas">
    <section class="business-card" aria-label="Quillstone Funeral Services business card">
      <svg class="card-ring" width="900" height="500" viewBox="0 0 900 500" aria-hidden="true">
        <circle cx="-40" cy="240" r="405" fill="none" stroke="#ffffff" stroke-width="8"/>
      </svg>
      <div class="dove-symbol" role="img" aria-label="White dove silhouette in flight, symbol of peace and eternal happiness"></div>
      <div class="contact-block">
        <p class="company-name">Quillstone Funeral Services</p>
        <p class="phone">+639174826351</p>
        <p class="email">darvik4521@pelmora.com</p>
        <p class="street">Corner of Brisco Ave. &amp; Velhurst St.</p>
        <p class="city-line">Makati City, Philippines</p>
      </div>
    </section>
  </main>
</body>
</html>
```